Vortane Labs - Methylene Blue Product Packaging

Our brand is Vortane Labs. We are launching a new product that is Methylene Blue, you can see more about this product if you search on Brisko or Pelludo and you will see what it is. This will be for a 50ml bottle. Give me different options for packaging that is minimalist and clean for this brand that makes it look well made and make people want to buy. I've added examples of what the bottle shape will be and potential packaging shapes so you can make packaging on those based off of that.

```html
<!DOCTYPE html>
<html lang="en">
<head>
<meta charset="UTF-8">
<title>Vortane Labs – Methylene Blue Label</title>
<link rel="stylesheet" href="https://fonts.googleapis.com/css2?family=Montserrat:wght@300;500;800&family=Poppins:wght@600&display=swap">
<style>
  :root {
    --label-dark: #232122;
    --label-text: #ffffff;
    --accent-blue: #1c6ff2;
  }
  html, body {
    margin: 0;
    padding: 0;
    width: 1186px;
    height: 1200px;
    overflow: hidden;
    background: var(--label-dark);
  }
  .label {
    position: relative;
    width: 1186px;
    height: 1200px;
    background: var(--label-dark);
    color: var(--label-text);
  }
  .brand {
    position: absolute;
    right: 229px;
    top: 104px;
    text-align: right;
    font-family: "Poppins", sans-serif;
    font-weight: 600;
    color: var(--label-text);
    line-height: 1;
  }
  .brand-name {
    display: block;
    font-size: 104px;
    letter-spacing: -1px;
  }
  .brand-sub {
    display: block;
    font-size: 62px;
    margin-top: 2px;
  }
  .product-name {
    position: absolute;
    right: 236px;
    top: 462px;
    margin: 0;
    text-align: right;
    line-height: 1;
  }
  .product-name .compound {
    display: block;
    font-family: "Montserrat", sans-serif;
    font-weight: 800;
    font-size: 80px;
    letter-spacing: 0.5px;
  }
  .product-name .colour-word {
    display: block;
    font-family: "Montserrat", sans-serif;
    font-weight: 300;
    font-size: 124px;
    color: var(--accent-blue);
    margin-top: 14px;
    letter-spacing: 1px;
  }
  .benefit {
    margin: 0;
    font-family: "Montserrat", sans-serif;
    font-weight: 500;
    font-size: 42px;
    line-height: 1;
    color: var(--label-text);
  }
  .benefit-line {
    position: absolute;
    right: 452px;
    white-space: nowrap;
  }
  .benefit-line.upper { top: 946px; }
  .benefit-line.lower { top: 1026px; }
  .strength-mark {
    position: absolute;
    left: 0;
    top: 0;
    width: 1186px;
    height: 1200px;
  }
  .strength-mark .rule,
  .strength-mark .hexagon {
    fill: none;
    stroke: var(--accent-blue);
    stroke-width: 7;
    stroke-linejoin: miter;
  }
  .strength-mark .strength-value {
    font-family: "Montserrat", sans-serif;
    font-weight: 500;
    font-size: 76px;
    fill: var(--label-text);
  }
</style>
</head>
<body>
  <main class="label">
    <div class="brand">
      <span class="brand-name">Vortane</span>
      <span class="brand-sub">Labs</span>
    </div>

    <h1 class="product-name">
      <span class="compound">Methylene</span>
      <span class="colour-word">BLUE</span>
    </h1>

    <svg class="strength-mark" viewBox="0 0 1186 1200" aria-hidden="true">
      <polyline class="rule" points="246,1010 749,1010"/>
      <polygon class="hexagon" points="749,1010 796,927 892,927 939,1010 892,1093 796,1093"/>
      <text class="strength-value" x="844" y="1037" text-anchor="middle">1%</text>
    </svg>

    <p class="benefit">
      <span class="benefit-line upper">Improves brain</span>
      <span class="benefit-line lower">performance</span>
    </p>
  </main>
</body>
</html>
```